Elegant Business Cards & Letterhead

We will need the following that need to be designed: Letterhead and Business Cards, there winer will be re-hired for the balance of our stationary needs. Text for the cards and letterheads:

- Corporate Card instead of name
- landline: +971 (4) 362 7041
- mobile: +971 56 2819 605
- 800TUTOR
- email: dubai@velmora-lune.com
- www.velmora-lune.com
- PO Box 387261
Address: Castellan Heights Suite 1708, Dubai UAE

Thank you

Target Market(s)

VIPs, HNWI, High-end Families.

Industry/Entity Type

Luxury Market

Font styles to use
Other font styles liked:
• as explained

Colors

Designer to choose only greyscale colors for use in the design.

Requirements
Must have
• Elegant, Simple, Luxurious, Minimalistic
Nice to have
• Luxury, Golds, Engravings,
Should not have
• Much colors, funky,

```html
<!DOCTYPE html>
<html lang="en">
<head>
<meta charset="utf-8">
<title>Velmora Lune — Stationery</title>
<link rel="stylesheet" href="https://fonts.googleapis.com/css2?family=Marcellus&family=Source+Serif+4:wght@300;400&display=swap">
<style>
  :root {
    --backdrop: #ada192;
    --paper: #ffffff;
    --ink: #2a2a2a;
    --gold-dark: #c8951f;
    --gold-mid: #e2b93b;
    --gold-light: #f5dc7a;
    --gold-text: #d4a22e;
    --gold-band: linear-gradient(90deg, var(--gold-dark) 0%, var(--gold-light) 45%, var(--gold-mid) 75%, var(--gold-dark) 100%);
  }
  * { margin: 0; padding: 0; box-sizing: border-box; }
  html, body { width: 1200px; height: 979px; overflow: hidden; }
  body {
    background: var(--backdrop);
    position: relative;
    font-family: "Source Serif 4", Georgia, serif;
    color: var(--ink);
  }
  .sheet { position: absolute; background: var(--paper); overflow: hidden; }
  .sheet svg.art { position: absolute; inset: 0; width: 100%; height: 100%; }
  .brand {
    font-family: "Marcellus", Georgia, serif;
    font-weight: 400;
    letter-spacing: 0.01em;
    white-space: nowrap;
    color: var(--ink);
    line-height: 1;
  }
  .masthead {
    position: absolute;
    left: 0;
    right: 0;
    height: 20px;
    display: flex;
    align-items: center;
  }
  .rule-pair {
    flex: 1;
    display: flex;
    flex-direction: column;
    justify-content: space-between;
  }
  .rule-pair span { display: block; height: 3.5px; background: var(--gold-band); }
  .contact {
    position: absolute;
    font-weight: 300;
    color: var(--ink);
  }
  .contact span { display: block; }

  /* Business card front */
  .card-front { left: 193px; top: 320px; width: 207px; height: 118px; border-radius: 6px; }
  .card-front .masthead { top: 48px; }
  .card-front .brand { margin-left: 20px; margin-right: 10px; font-size: 17.5px; }
  .card-front .rule-pair { height: 12.5px; }

  /* Business card back */
  .card-back { left: 193px; top: 514px; width: 207px; height: 118px; border-radius: 6px; }
  .card-back .brand { position: absolute; right: 13px; top: 21px; font-size: 10px; color: var(--gold-text); }
  .card-back .holder { position: absolute; left: 11px; top: 37px; font-size: 8.5px; font-weight: 300; line-height: 1; }
  .card-back .contact { left: 17px; top: 82px; font-size: 5.8px; line-height: 1.5; }

  /* Letterhead */
  .letterhead { left: 517px; top: 143px; width: 490px; height: 693px; }
  .letterhead .masthead { top: 38px; }
  .letterhead .brand { margin-left: 32px; margin-right: 17px; font-size: 18px; }
  .letterhead .rule-pair { height: 12px; }
  .letterhead .contact { left: 21px; top: 647px; font-size: 7.8px; line-height: 1.45; }
</style>
</head>
<body>

<section class="sheet card-front" aria-label="Business card, front">
  <svg class="art" viewBox="0 0 207 118" preserveAspectRatio="none" aria-hidden="true">
    <defs>
      <linearGradient id="goldFront" x1="0" y1="0" x2="1" y2="1">
        <stop offset="0" stop-color="var(--gold-dark)"/>
        <stop offset="0.5" stop-color="var(--gold-light)"/>
        <stop offset="1" stop-color="var(--gold-mid)"/>
      </linearGradient>
    </defs>
    <polygon points="0,49 8.5,58 0,67" fill="url(#goldFront)"/>
    <polygon points="176,118 185,109 194,118" fill="url(#goldFront)"/>
  </svg>
  <div class="masthead">
    <div class="brand">VELMORA LUNE</div>
    <div class="rule-pair" aria-hidden="true"><span></span><span></span></div>
  </div>
</section>

<section class="sheet card-back" aria-label="Business card, back">
  <svg class="art" viewBox="0 0 207 118" preserveAspectRatio="none" aria-hidden="true">
    <defs>
      <linearGradient id="goldBack" x1="0" y1="0" x2="1" y2="1">
        <stop offset="0" stop-color="var(--gold-dark)"/>
        <stop offset="0.5" stop-color="var(--gold-light)"/>
        <stop offset="1" stop-color="var(--gold-mid)"/>
      </linearGradient>
    </defs>
    <polygon points="176,0 194,0 185,9" fill="url(#goldBack)"/>
    <rect x="11.5" y="83" width="1.5" height="24" fill="url(#goldBack)"/>
  </svg>
  <div class="brand">VELMORA LUNE</div>
  <p class="holder">Name here</p>
  <p class="contact"><span>Address</span><span>Email</span><span>Web.</span></p>
</section>

<section class="sheet letterhead" aria-label="Letterhead">
  <svg class="art" viewBox="0 0 490 693" preserveAspectRatio="none" aria-hidden="true">
    <defs>
      <linearGradient id="goldSheet" x1="0" y1="0" x2="1" y2="1">
        <stop offset="0" stop-color="var(--gold-dark)"/>
        <stop offset="0.5" stop-color="var(--gold-light)"/>
        <stop offset="1" stop-color="var(--gold-mid)"/>
      </linearGradient>
    </defs>
    <polygon points="0,33 15,48 0,63" fill="url(#goldSheet)"/>
    <rect x="14" y="649" width="2" height="31" fill="url(#goldSheet)"/>
    <polygon points="418,693 441.5,670 465,693" fill="url(#goldSheet)"/>
  </svg>
  <div class="masthead">
    <div class="brand">VELMORA LUNE</div>
    <div class="rule-pair" aria-hidden="true"><span></span><span></span></div>
  </div>
  <p class="contact"><span>Address</span><span>Email</span><span>Web.</span></p>
</section>

</body>
</html>
```